Equity, Effectiveness and Efficiency in charitable food relief sector

I am undertaking my PhD in food policy in the charitable food relief sector, specifically investigating the factors (supply, demand and capacity) that affect the introduction of nutrition policy and in turn, affect the sector's ability to achieve equity, effectiveness and efficiency.

I need a graphic device that incorporates this central idea of Equity, Effectiveness and Efficiency, and how the factors of supply, demand and capacity interact. There are sub-factors within supply (1-6), demand (7-10) and capacity (11 - 15). All these details are shown in the attached figure (Basic figure_Eq Effec Effic and factors.jpg)

This figure (Basic figure_Eq Effec Effic and factors.jpg) contains all the information I need in a graphic but I need something that is more visually appealing, and that can link the ideas in a format other than a table. The final graphic will outline how the food relief sector balances the core objectives of equity, effectiveness and efficiency with the factors (and sub-factors) of supply, demand and capacity.

```html
<!DOCTYPE html>
<html lang="en">
<head>
<meta charset="utf-8">
<title>Factors affecting the introduction of nutrition policy</title>
<link rel="stylesheet" href="https://fonts.googleapis.com/css2?family=Roboto:wght@500;700;900&display=swap">
<style>
  :root {
    --bg: #ebebed;
    --ink: #141414;
    --line: #2a2a2a;
    --core: #e07d14;
    --supply: #52519e;
    --demand: #40a0bd;
    --capacity: #c1106d;
    --storage-sub: #7a3583;
    --workforce-sub: #e07b14;
    --white: #ffffff;
  }
  html, body {
    margin: 0;
    padding: 0;
    width: 926px;
    height: 1200px;
    overflow: hidden;
    background: var(--bg);
  }
  .poster {
    position: relative;
    width: 926px;
    height: 1200px;
    font-family: "Roboto", Arial, sans-serif;
  }
  .poster-title {
    position: absolute;
    top: 56px;
    left: 0;
    width: 926px;
    margin: 0;
    text-align: center;
    font-weight: 900;
    font-size: 33px;
    line-height: 53px;
    color: var(--ink);
  }
  .diagram { position: absolute; top: 0; left: 0; }
  .connector { fill: none; stroke: var(--line); stroke-width: 1; }
  .trunk { fill: none; stroke: var(--line); stroke-width: 1.4; }
  .joint { fill: var(--line); }
  .core-label { font-weight: 700; font-size: 18.5px; fill: var(--ink); text-anchor: middle; }
  .hub-label { font-weight: 500; font-size: 12px; fill: var(--ink); text-anchor: middle; }
  .tag-label { font-weight: 500; font-size: 7.2px; fill: var(--white); }
  .tag-label.large { font-size: 8.4px; }
  .tag-label.small { font-size: 5.3px; }
  .supply .tag { fill: var(--supply); }
  .demand .tag { fill: var(--demand); }
  .capacity .tag { fill: var(--capacity); }
  .storage-sub .tag { fill: var(--storage-sub); }
  .workforce-sub .tag { fill: var(--workforce-sub); }
  .supply .icon { fill: var(--supply); }
  .demand .icon { fill: var(--demand); }
  .capacity .icon { fill: var(--capacity); }
  .storage-sub .icon { fill: var(--storage-sub); }
  .workforce-sub .icon { fill: var(--workforce-sub); }
  .icon { opacity: 0.22; }
</style>
</head>
<body>
<div class="poster">
  <h1 class="poster-title">Factors affecting the introduction of<br>nutrition policy</h1>

  <svg class="diagram" width="926" height="1200" viewBox="0 0 926 1200" xmlns="http://www.w3.org/2000/svg">
    <defs>
      <linearGradient id="disc" x1="0" y1="0" x2="0" y2="1">
        <stop offset="0" stop-color="#fbfbfc"/>
        <stop offset="1" stop-color="#d4d4d7"/>
      </linearGradient>
      <filter id="soft" x="-30%" y="-30%" width="160%" height="160%">
        <feDropShadow dx="0" dy="1" stdDeviation="1.2" flood-color="#000" flood-opacity="0.25"/>
      </filter>
      <g id="tag-l"><path class="tag-shape" d="M0 -14.5 H71 L76 0 L71 14.5 H0 Z"/></g>
    </defs>

    <!-- core to hubs -->
    <path class="trunk" d="M305 634 H328 Q343 634 343 619 V386 Q343 371 358 371 H421"/>
    <path class="trunk" d="M305 682 H421"/>
    <path class="trunk" d="M305 729 H328 Q343 729 343 744 V976 Q343 991 358 991 H421"/>
    <g class="joint">
      <circle cx="305" cy="634" r="3.2"/><circle cx="305" cy="682" r="3.2"/><circle cx="305" cy="729" r="3.2"/>
      <circle cx="421" cy="371" r="3.2"/><circle cx="421" cy="682" r="3.2"/><circle cx="421" cy="991" r="3.2"/>
    </g>

    <!-- core -->
    <g class="core">
      <circle cx="176" cy="681" r="91" fill="url(#disc)" stroke="var(--core)" stroke-width="13"/>
      <text class="core-label" x="176" y="664">Equity ,</text>
      <text class="core-label" x="176" y="689">Effectiveness ,</text>
      <text class="core-label" x="176" y="713">Efficiency</text>
    </g>

    <!-- hubs -->
    <g class="hub">
      <path class="connector" d="M490 322 A49 49 0 0 1 490 420"/>
      <circle class="joint" cx="490" cy="322" r="1.6"/><circle class="joint" cx="490" cy="420" r="1.6"/>
      <circle cx="490" cy="371" r="39" fill="url(#disc)" stroke="var(--supply)" stroke-width="4.5"/>
      <circle class="icon" cx="490" cy="361" r="11" fill="var(--supply)" role="img" aria-label="Supply network icon"/>
      <text class="hub-label" x="490" y="390">Supply</text>
    </g>
    <g class="hub">
      <path class="connector" d="M490 633 A49 49 0 0 1 490 731"/>
      <circle class="joint" cx="490" cy="633" r="1.6"/><circle class="joint" cx="490" cy="731" r="1.6"/>
      <circle cx="490" cy="682" r="39" fill="url(#disc)" stroke="var(--demand)" stroke-width="4.5"/>
      <circle class="icon" cx="490" cy="672" r="11" fill="var(--demand)" role="img" aria-label="Demand growth icon"/>
      <text class="hub-label" x="490" y="702">Demand</text>
    </g>
    <g class="hub">
      <path class="connector" d="M490 945 A49 49 0 0 1 490 1043"/>
      <circle class="joint" cx="490" cy="945" r="1.6"/><circle class="joint" cx="490" cy="1043" r="1.6"/>
      <circle cx="490" cy="994" r="39" fill="url(#disc)" stroke="var(--capacity)" stroke-width="4.5"/>
      <circle class="icon" cx="490" cy="984" r="11" fill="var(--capacity)" role="img" aria-label="Capacity icon"/>
      <text class="hub-label" x="490" y="1014">Capacity</text>
    </g>

    <!-- branches -->
    <g class="connector">
      <path d="M546 352 H555 Q561 352 561 346 V252 Q561 246 567 246 H594"/>
      <path d="M546 359 H563 Q569 359 569 353 V300 Q569 294 575 294 H594"/>
      <path d="M546 366 H572 Q578 366 578 360 V348 Q578 342 584 342 H594"/>
      <path d="M546 373 H574 Q580 373 580 379 V391 Q580 397 586 397 H594"/>
      <path d="M546 380 H566 Q572 380 572 386 V440 Q572 446 578 446 H594"/>
      <path d="M546 387 H558 Q564 387 564 393 V488 Q564 494 570 494 H594"/>
      <path d="M546 671 H565 Q571 671 571 665 V612 Q571 606 577 606 H594"/>
      <path d="M546 678 H572 Q578 678 578 672 V659 Q578 653 584 653 H594"/>
      <path d="M546 685 H573 Q579 685 579 691 V704 Q579 710 585 710 H594"/>
      <path d="M546 692 H567 Q573 692 573 698 V751 Q573 757 579 757 H594"/>
      <path d="M546 976 H556 Q562 976 562 970 V875 Q562 869 568 869 H594"/>
      <path d="M546 984 H565 Q571 984 571 978 V923 Q571 917 577 917 H594"/>
      <path d="M546 993 H594"/>
      <path d="M546 1001 H565 Q571 1001 571 1007 V1062 Q571 1068 577 1068 H594"/>
      <path d="M546 1009 H556 Q562 1009 562 1015 V1111 Q562 1117 568 1117 H594"/>
      <path d="M717 866 H737 Q743 866 743 860 V854 Q743 848 749 848 H755"/>
      <path d="M717 872 H737 Q743 872 743 878 V881 Q743 887 749 887 H755"/>
      <path d="M725 982 H730 Q736 982 736 976 V932 Q736 926 742 926 H752"/>
      <path d="M725 988 H733 Q739 988 739 982 V968 Q739 962 745 962 H752"/>
      <path d="M725 995 H752"/>
      <path d="M725 1001 H733 Q739 1001 739 1007 V1026 Q739 1032 745 1032 H752"/>
      <path d="M725 1007 H730 Q736 1007 736 1013 V1059 Q736 1065 742 1065 H752"/>
    </g>
    <g class="joint">
      <circle cx="546" cy="352" r="1.4"/><circle cx="546" cy="359" r="1.4"/><circle cx="546" cy="366" r="1.4"/>
      <circle cx="546" cy="373" r="1.4"/><circle cx="546" cy="380" r="1.4"/><circle cx="546" cy="387" r="1.4"/>
      <circle cx="546" cy="671" r="1.4"/><circle cx="546" cy="678" r="1.4"/><circle cx="546" cy="685" r="1.4"/><circle cx="546" cy="692" r="1.4"/>
      <circle cx="546" cy="976" r="1.4"/><circle cx="546" cy="984" r="1.4"/><circle cx="546" cy="993" r="1.4"/><circle cx="546" cy="1001" r="1.4"/><circle cx="546" cy="1009" r="1.4"/>
      <circle cx="594" cy="246" r="1.4"/><circle cx="594" cy="294" r="1.4"/><circle cx="594" cy="342" r="1.4"/>
      <circle cx="594" cy="397" r="1.4"/><circle cx="594" cy="446" r="1.4"/><circle cx="594" cy="494" r="1.4"/>
      <circle cx="594" cy="606" r="1.4"/><circle cx="594" cy="653" r="1.4"/><circle cx="594" cy="710" r="1.4"/><circle cx="594" cy="757" r="1.4"/>
      <circle cx="594" cy="869" r="1.4"/><circle cx="594" cy="917" r="1.4"/><circle cx="594" cy="993" r="1.4"/><circle cx="594" cy="1068" r="1.4"/><circle cx="594" cy="1117" r="1.4"/>
      <circle cx="717" cy="866" r="1.4"/><circle cx="717" cy="872" r="1.4"/><circle cx="755" cy="848" r="1.4"/><circle cx="755" cy="887" r="1.4"/>
      <circle cx="725" cy="982" r="1.2"/><circle cx="725" cy="988" r="1.2"/><circle cx="725" cy="995" r="1.2"/><circle cx="725" cy="1001" r="1.2"/><circle cx="725" cy="1007" r="1.2"/>
      <circle cx="752" cy="926" r="1.2"/><circle cx="752" cy="962" r="1.2"/><circle cx="752" cy="995" r="1.2"/><circle cx="752" cy="1032" r="1.2"/><circle cx="752" cy="1065" r="1.2"/>
    </g>

    <!-- supply factors -->
    <g class="supply">
      <g transform="translate(620 246)"><path class="tag" d="M10 -14.5 H87 L92 0 L87 14.5 H10 Z"/><circle r="20" fill="url(#disc)" stroke="#fff" stroke-width="2" filter="url(#soft)"/><circle class="icon" r="11" role="img" aria-label="Warehouses and truck icon"/><text class="tag-label" x="28" y="-2">Uncertain</text><text class="tag-label" x="28" y="8">material supply</text></g>
      <g transform="translate(620 294)"><path class="tag" d="M10 -14.5 H87 L92 0 L87 14.5 H10 Z"/><circle r="20" fill="url(#disc)" stroke="#fff" stroke-width="2" filter="url(#soft)"/><circle class="icon" r="11" role="img" aria-label="Parcel delivery icon"/><text class="tag-label" x="28" y="-2">Uncertain</text><text class="tag-label" x="28" y="8">Monetary Supply</text></g>
      <g transform="translate(620 342)"><path class="tag" d="M10 -14.5 H87 L92 0 L87 14.5 H10 Z"/><circle r="20" fill="url(#disc)" stroke="#fff" stroke-width="2" filter="url(#soft)"/><circle class="icon" r="11" role="img" aria-label="Grocery bag icon"/><text class="tag-label" x="28" y="-2">Limited food</text><text class="tag-label" x="28" y="8">supply</text></g>
      <g transform="translate(620 397)"><path class="tag" d="M10 -14.5 H87 L92 0 L87 14.5 H10 Z"/><circle r="20" fill="url(#disc)" stroke="#fff" stroke-width="2" filter="url(#soft)"/><circle class="icon" r="11" role="img" aria-label="Food with timer icon"/><text class="tag-label" x="28" y="3">Perishability</text></g>
      <g transform="translate(620 446)"><path class="tag" d="M10 -14.5 H87 L92 0 L87 14.5 H10 Z"/><circle r="20" fill="url(#disc)" stroke="#fff" stroke-width="2" filter="url(#soft)"/><circle class="icon" r="11" role="img" aria-label="Constraint magnet icon"/><text class="tag-label" x="28" y="3">Donor Constraints</text></g>
      <g transform="translate(620 494)"><path class="tag" d="M10 -14.5 H87 L92 0 L87 14.5 H10 Z"/><circle r="20" fill="url(#disc)" stroke="#fff" stroke-width="2" filter="url(#soft)"/><circle class="icon" r="11" role="img" aria-label="Donor group icon"/><text class="tag-label" x="28" y="-2">Donor</text><text class="tag-label" x="28" y="8">relationships</text></g>
    </g>

    <!-- demand factors -->
    <g class="demand">
      <g transform="translate(620 606)"><path class="tag" d="M10 -14.5 H87 L92 0 L87 14.5 H10 Z"/><circle r="20" fill="url(#disc)" stroke="#fff" stroke-width="2" filter="url(#soft)"/><circle class="icon" r="11" role="img" aria-label="Question icon"/><text class="tag-label large" x="28" y="-2">Uncertain</text><text class="tag-label large" x="28" y="8">demand</text></g>
      <g transform="translate(620 653)"><path class="tag" d="M10 -14.5 H87 L92 0 L87 14.5 H10 Z"/><circle r="20" fill="url(#disc)" stroke="#fff" stroke-width="2" filter="url(#soft)"/><circle class="icon" r="11" role="img" aria-label="Visibility window icon"/><text class="tag-label large" x="28" y="-2">Limited demand</text><text class="tag-label large" x="28" y="8">visibility</text></g>
      <g transform="translate(620 710)"><path class="tag" d="M10 -14.5 H87 L92 0 L87 14.5 H10 Z"/><circle r="20" fill="url(#disc)" stroke="#fff" stroke-width="2" filter="url(#soft)"/><circle class="icon" r="11" role="img" aria-label="Clients in hand icon"/><text class="tag-label large" x="28" y="3">Clients Choice</text></g>
      <g transform="translate(620 757)"><path class="tag" d="M10 -14.5 H87 L92 0 L87 14.5 H10 Z"/><circle r="20" fill="url(#disc)" stroke="#fff" stroke-width="2" filter="url(#soft)"/><circle class="icon" r="11" role="img" aria-label="Food bowl icon"/><text class="tag-label large" x="28" y="3">Food Wastage</text></g>
    </g>

    <!-- capacity factors -->
    <g class="capacity">
      <g transform="translate(620 869)"><path class="tag" d="M10 -14.5 H87 L92 0 L87 14.5 H10 Z"/><circle r="20" fill="url(#disc)" stroke="#fff" stroke-width="2" filter="url(#soft)"/><circle class="icon" r="11" role="img" aria-label="Storage building icon"/><text class="tag-label large" x="28" y="3">Storage</text></g>
      <g transform="translate(620 917)"><path class="tag" d="M10 -14.5 H87 L92 0 L87 14.5 H10 Z"/><circle r="20" fill="url(#disc)" stroke="#fff" stroke-width="2" filter="url(#soft)"/><circle class="icon" r="11" role="img" aria-label="Transport icon"/><text class="tag-label large" x="28" y="3">Transporation</text></g>
      <g transform="translate(620 994)"><path class="tag" d="M10 -14.5 H87 L92 0 L87 14.5 H10 Z"/><circle r="20" fill="url(#disc)" stroke="#fff" stroke-width="2" filter="url(#soft)"/><circle class="icon" r="11" role="img" aria-label="Workforce team icon"/><text class="tag-label large" x="28" y="3">Workforce</text></g>
      <g transform="translate(620 1068)"><path class="tag" d="M10 -14.5 H87 L92 0 L87 14.5 H10 Z"/><circle r="20" fill="url(#disc)" stroke="#fff" stroke-width="2" filter="url(#soft)"/><circle class="icon" r="11" role="img" aria-label="Stakeholder network icon"/><text class="tag-label large" x="28" y="-2">External</text><text class="tag-label large" x="28" y="8">Stakeholders</text></g>
      <g transform="translate(620 1117)"><path class="tag" d="M10 -14.5 H87 L92 0 L87 14.5 H10 Z"/><circle r="20" fill="url(#disc)" stroke="#fff" stroke-width="2" filter="url(#soft)"/><circle class="icon" r="11" role="img" aria-label="Budget icon"/><text class="tag-label large" x="28" y="3">Budget</text></g>
    </g>

    <!-- storage types -->
    <g class="storage-sub">
      <g transform="translate(785 848)"><path class="tag" d="M8 -10 H59 L63 0 L59 10 H8 Z"/><circle r="14" fill="url(#disc)" stroke="#fff" stroke-width="1.5" filter="url(#soft)"/><circle class="icon" r="7.5" role="img" aria-label="Thermometer icon"/><text class="tag-label small" x="19" y="2">Cold</text></g>
      <g transform="translate(785 887)"><path class="tag" d="M8 -10 H59 L63 0 L59 10 H8 Z"/><circle r="14" fill="url(#disc)" stroke="#fff" stroke-width="1.5" filter="url(#soft)"/><circle class="icon" r="7.5" role="img" aria-label="Warehouse icon"/><text class="tag-label small" x="19" y="2">Warehouse</text></g>
    </g>

    <!-- workforce aspects -->
    <g class="workforce-sub">
      <g transform="translate(785 926)"><path class="tag" d="M8 -10 H59 L63 0 L59 10 H8 Z"/><circle r="14" fill="url(#disc)" stroke="#fff" stroke-width="1.5" filter="url(#soft)"/><circle class="icon" r="7.5" role="img" aria-label="Volunteers icon"/><text class="tag-label small" x="19" y="2">Volunteers</text></g>
      <g transform="translate(785 962)"><path class="tag" d="M8 -10 H59 L63 0 L59 10 H8 Z"/><circle r="14" fill="url(#disc)" stroke="#fff" stroke-width="1.5" filter="url(#soft)"/><circle class="icon" r="7.5" role="img" aria-label="Training icon"/><text class="tag-label small" x="19" y="-1">Expertise and</text><text class="tag-label small" x="19" y="5.5">training</text></g>
      <g transform="translate(785 995)"><path class="tag" d="M8 -10 H59 L63 0 L59 10 H8 Z"/><circle r="14" fill="url(#disc)" stroke="#fff" stroke-width="1.5" filter="url(#soft)"/><circle class="icon" r="7.5" role="img" aria-label="Benefits icon"/><text class="tag-label small" x="19" y="-1">Attitutes and</text><text class="tag-label small" x="19" y="5.5">Benefits</text></g>
      <g transform="translate(785 1032)"><path class="tag" d="M8 -10 H59 L63 0 L59 10 H8 Z"/><circle r="14" fill="url(#disc)" stroke="#fff" stroke-width="1.5" filter="url(#soft)"/><circle class="icon" r="7.5" role="img" aria-label="Collaboration icon"/><text class="tag-label small" x="19" y="2">Collaboration</text></g>
      <g transform="translate(785 1065)"><path class="tag" d="M8 -10 H59 L63 0 L59 10 H8 Z"/><circle r="14" fill="url(#disc)" stroke="#fff" stroke-width="1.5" filter="url(#soft)"/><circle class="icon" r="7.5" role="img" aria-label="Executive support icon"/><text class="tag-label small" x="19" y="-1">Executive</text><text class="tag-label small" x="19" y="5.5">Support</text></g>
    </g>
  </svg>
</div>
</body>
</html>
```